Business Card Design Project

I need some business cards with the logo you did for us (attached)
I am looking for a coulourful yet serious business card

We do market research
on the back I want the logo

on the front my name : Corinne Valdessac
position : Manager
address : Brume Analytica Sarl - 27 Rue des tanneurs
1847 Glarency - Switzerland
corinne.valdessac@brumeanalytica.ch
Tel : +4122 934 07 58
Mob France :+33 671 42 8356
Mob Italy +39 347 520 8163

The tree of the logo could also be used alone

THE BACKGROUND COLOR ON THE FRONT HAS TO BE WHITE, ON THE BACK YU CAN TRY OHER COLOUR BUT HOMOGENEOUS (NOT EXPENSIVE TO PRINT)

Target Market(s)

multinational companies or other market research companies

Industry/Entity Type

Market Research

Requirements
Must have
• logo on the back
and all the info above

```html
<!DOCTYPE html>
<html lang="en">
<head>
<meta charset="utf-8">
<title>Brume Analytica – Business Card</title>
<link rel="stylesheet" href="https://fonts.googleapis.com/css2?family=Open+Sans:wght@400;600;700&display=swap">
<style>
  :root {
    --backdrop: #e9e6e1;
    --card-white: #ffffff;
    --card-grey: #f1f1f1;
    --green-light: #a9cd4a;
    --green-dark: #6a9f1e;
    --green-rule: #8dba2f;
    --crimson: #b8194a;
    --ink-dark: #2b2f33;
    --mark-grey: #d8d8d8;
  }
  * { box-sizing: border-box; margin: 0; padding: 0; }
  html, body { width: 1200px; height: 723px; overflow: hidden; }
  body {
    background: var(--backdrop);
    font-family: "Open Sans", Arial, sans-serif;
    display: flex;
    align-items: center;
    justify-content: center;
    gap: 80px;
  }
  .card {
    position: relative;
    width: 380px;
    height: 610px;
    background: var(--card-white);
    box-shadow: 0 6px 18px rgba(0,0,0,0.18);
    overflow: hidden;
  }

  /* Back side */
  .card--back {
    background: linear-gradient(180deg, var(--card-white) 0%, var(--card-grey) 100%);
  }
  .back__mark {
    position: absolute;
    left: 50%;
    top: 110px;
    transform: translateX(-50%);
  }
  .back__web {
    position: absolute;
    left: 0;
    right: 0;
    bottom: 38px;
    text-align: center;
    color: var(--crimson);
    font-weight: 700;
    font-size: 20px;
    letter-spacing: 3px;
  }

  /* Front side */
  .front__head {
    height: 200px;
    background: linear-gradient(180deg, var(--card-white) 0%, var(--card-grey) 100%);
    display: flex;
    align-items: center;
    justify-content: center;
    gap: 10px;
    padding-top: 20px;
  }
  .front__dot {
    width: 14px;
    height: 14px;
    border-radius: 50%;
    background: var(--crimson);
  }
  .front__brand {
    color: var(--crimson);
    font-weight: 600;
    font-size: 36px;
    letter-spacing: -0.5px;
  }
  .front__rule {
    height: 10px;
    border-top: 3px solid var(--green-rule);
    border-bottom: 3px solid var(--green-rule);
    background: var(--card-white);
  }
  .front__body {
    height: 400px;
    background: linear-gradient(160deg, var(--green-light) 0%, var(--green-dark) 100%);
    text-align: center;
    color: var(--card-white);
    padding-top: 60px;
  }
  .front__name {
    font-weight: 700;
    font-size: 22px;
  }
  .front__role {
    color: var(--ink-dark);
    font-weight: 700;
    font-size: 13px;
    margin-top: 1px;
  }
  .front__address {
    font-size: 14.5px;
    line-height: 1.45;
    margin-top: 28px;
  }
  .front__phones {
    font-size: 14.5px;
    line-height: 1.45;
    margin-top: 30px;
  }
  .front__email {
    color: var(--crimson);
    font-weight: 700;
    font-size: 14px;
    margin-top: 2px;
  }
</style>
</head>
<body>
  <section class="card card--back">
    <svg class="back__mark" width="230" height="230" viewBox="0 0 230 230" role="img" aria-label="Faint brand symbol area">
      <circle cx="115" cy="115" r="110" fill="var(--mark-grey)" opacity="0.55"/>
    </svg>
    <p class="back__web">www.brumeanalytica.ch</p>
  </section>

  <section class="card card--front">
    <header class="front__head">
      <span class="front__dot"></span>
      <span class="front__brand">brume analytica</span>
    </header>
    <div class="front__rule"></div>
    <div class="front__body">
      <h1 class="front__name">Corinne Valdessac</h1>
      <p class="front__role">Manager</p>
      <p class="front__address">Brume Analytica Sarl - 27 Rue des tanneurs<br>1847 Glarency - Switzerland</p>
      <p class="front__phones">PH: +4122-934-07 58<br>Mob France: +33-671-42-8356<br>Mob Italy: +39-347-520-8163</p>
      <p class="front__email">corinne.valdessac@brumeanalytica.ch</p>
    </div>
  </section>
</body>
</html>
```